Geschäftspapiere für Kanzlei
Zielgruppe
Forschungsinstitute und Großunternehmen die eigene Entwicklungsabteilungen haben und Erfindungen patentieren lassen.
Aufgabenstellung
Möglicherweise ergibt eine Weiterentwiklung unseres logos Sinn? Denkbar wäre für uns aber auch auf das Logo ganz zu verzichten.
Es sollte nicht mehr als eine Farbe (Blauton) verwendet werden. Wir wollen schlicht, klassisch und seriös auftreten.

```html
<!DOCTYPE html>
<html lang="de">
<head>
<meta charset="utf-8">
<title>Briefbogen – Kanzlei Dr. Sardelis</title>
<link rel="stylesheet" href="https://fonts.googleapis.com/css2?family=Noto+Sans:wght@400;700&display=swap">
<style>
  :root {
    --navy: #0d2b55;
    --ink: #111111;
    --frame: #1c1c1c;
    --paper: #ffffff;
  }
  html, body {
    margin: 0;
    padding: 0;
    width: 848px;
    height: 1200px;
    overflow: hidden;
    background: var(--paper);
  }
  .letterhead {
    position: relative;
    width: 848px;
    height: 1200px;
    box-sizing: border-box;
    border: 2px solid var(--frame);
    background: var(--paper);
    font-family: "Noto Sans", Arial, sans-serif;
    color: var(--navy);
    overflow: hidden;
  }
  .brand-name {
    position: absolute;
    left: 234px;
    top: 22px;
    width: 60px;
    height: 57px;
    display: flex;
    flex-direction: column;
    align-items: center;
    justify-content: center;
    gap: 6px;
    font-weight: 700;
    font-size: 11px;
    color: var(--navy);
  }
  .brand-name .mark {
    width: 18px;
    height: 18px;
    background: var(--navy);
  }
  .header-titles {
    position: absolute;
    left: 309px;
    top: 20px;
    font-size: 12.8px;
    line-height: 15.4px;
    letter-spacing: 0.35px;
  }
  .header-titles strong { font-weight: 700; }
  .header-titles p { margin: 0; }
  .sender-line {
    position: absolute;
    left: 96px;
    top: 180px;
    font-size: 8.4px;
    color: var(--ink);
    margin: 0;
  }
  .fold-mark {
    position: absolute;
    left: 0;
    top: 401px;
    width: 10px;
    height: 0;
    border-top: 1px solid var(--ink);
  }
  .footer-block {
    position: absolute;
    top: 1153px;
    font-size: 10.2px;
    line-height: 13px;
    letter-spacing: 0.2px;
    margin: 0;
  }
  .footer-block p { margin: 0; }
  .footer-identity { left: 244px; }
  .footer-contact { left: 520px; }
  .footer-identity strong { font-weight: 700; }
</style>
</head>
<body>
  <main class="letterhead">
    <div class="brand-name"><span class="mark"></span><span>Sardelis</span></div>

    <header class="header-titles">
      <p><strong>Dr. rer. nat. Levan Sardelis</strong> PhD</p>
      <p>Patentanwalt</p>
      <p>European Patent Attorney</p>
      <p>European Design- und Trademark Attorney</p>
    </header>

    <p class="sender-line">Kanzlei Dr. Sardelis • Lindenhofstrasse 22 • 80339 München</p>

    <span class="fold-mark"></span>

    <footer>
      <div class="footer-block footer-identity">
        <p><strong>Dr. rer. nat. Levan Sardelis&nbsp; · &nbsp;PhD</strong></p>
        <p>Patentanwalt &nbsp;· &nbsp;European Patent Attorney</p>
        <p>European Design- und Trademark Attorney</p>
      </div>
      <div class="footer-block footer-contact">
        <p>Lindenhofstrasse 22 &nbsp;· &nbsp;80339 München</p>
        <p>Tel. + 49 89 000 311 420 &nbsp;· &nbsp;Fax: + 49 89 000 311 49</p>
        <p>Email: office@sardelis-ip.de</p>
      </div>
    </footer>
  </main>
</body>
</html>
```